Inspiration Poster

Inspirational Poster that has a Kamran Dulo like abstract look (http://www.vexalo.com/images/search?q=kamran+dulo&FORM=HDRSC2) with the text:

"we walk not in order to arrive at the promise land but because walking itself is a revolution"
-Peter Ambrick

```html
<!DOCTYPE html>
<html lang="en">
<head>
<meta charset="utf-8">
<title>Walking Itself Is A Revolution — Poster</title>
<link rel="stylesheet" href="https://fonts.googleapis.com/css2?family=Playfair+Display:wght@700&display=swap">
<style>
  :root {
    --magenta: #ee1a55;
    --magenta-deep: #c8124c;
    --navy: #1c1652;
    --navy-soft: #4a1a5e;
    --ink: #ffffff;
  }
  html, body {
    margin: 0;
    padding: 0;
    overflow: hidden;
    background: var(--magenta);
  }
  .poster {
    position: relative;
    width: 849px;
    height: 1200px;
    overflow: hidden;
    font-family: "Playfair Display", "Times New Roman", serif;
    font-weight: 700;
    color: var(--ink);
  }
  .poster__photo {
    position: absolute;
    inset: 0;
    background:
      radial-gradient(ellipse 180px 520px at 230px 760px, rgba(28,22,82,0.85), rgba(28,22,82,0) 70%),
      radial-gradient(ellipse 140px 480px at 60px 700px, rgba(28,22,82,0.8), rgba(28,22,82,0) 70%),
      radial-gradient(ellipse 90px 300px at 740px 560px, rgba(28,22,82,0.75), rgba(28,22,82,0) 70%),
      linear-gradient(90deg, var(--navy-soft) 0%, var(--magenta-deep) 22%, var(--magenta) 45%, var(--magenta) 100%);
  }
  .quote {
    position: absolute;
    inset: 0;
    text-transform: uppercase;
  }
  .quote__line {
    position: absolute;
    left: 313px;
    margin: 0;
    line-height: 1;
    white-space: nowrap;
    transform-origin: left top;
    transform: scaleX(0.68);
  }
  .quote__line--lead {
    top: 224px;
    font-size: 99px;
  }
  .quote__line--body { font-size: 52px; }
  .quote__line--closing {
    top: 606px;
    font-size: 108px;
    text-transform: none;
    transform: scaleX(0.64);
  }
  .quote__author {
    position: absolute;
    top: 716px;
    right: 54px;
    margin: 0;
    font-size: 23px;
    line-height: 1;
    text-transform: none;
    transform-origin: right top;
    transform: scaleX(0.75);
    white-space: nowrap;
  }
</style>
</head>
<body>
  <main class="poster">
    <div class="poster__photo" role="img" aria-label="Motion-blurred crowd of people walking through a corridor, tinted magenta and deep navy"></div>
    <blockquote class="quote">
      <p class="quote__line quote__line--lead">We walk</p>
      <p class="quote__line quote__line--body" style="top:329px">Not in order</p>
      <p class="quote__line quote__line--body" style="top:387px">to arrive at</p>
      <p class="quote__line quote__line--body" style="top:444px">the promise land</p>
      <p class="quote__line quote__line--body" style="top:502px">but because</p>
      <p class="quote__line quote__line--body" style="top:560px">walking itself is</p>
      <p class="quote__line quote__line--closing">A Revolution.</p>
      <p class="quote__author">- Peter Ambrick</p>
    </blockquote>
  </main>
</body>
</html>
```